Plumwave business card

We need a modern business card - With our 4 colors - See web: www.plumwave.dk

I have attached logo and som old business Cards we have - Lets Make the new ones shine...:-) -

Industry/Entity Type

Business

Requirements
Must have
• the logo with plumwave only,

```html
<!DOCTYPE html>
<html lang="da">
<head>
<meta charset="utf-8">
<title>Plumwave business card</title>
<link rel="stylesheet" href="https://fonts.googleapis.com/css2?family=Source+Sans+3:wght@300;400;600&display=swap">
<style>
  :root {
    --backdrop: #1c1c1c;
    --paper: #ffffff;
    --plum: #722a7a;
    --magenta: #e6168c;
    --lime: #a8c63a;
    --lime-line: #a3c83c;
    --orange: #f0862a;
    --ink: #111111;
    --grey: #444444;
  }
  * { margin: 0; padding: 0; box-sizing: border-box; }
  html, body { width: 1200px; height: 900px; overflow: hidden; }
  body {
    background: var(--backdrop);
    font-family: "Source Sans 3", sans-serif;
    position: relative;
  }
  .card {
    position: absolute;
    top: 170px;
    width: 347px;
    height: 561px;
    overflow: hidden;
  }
  .card--front { left: 259px; background: var(--paper); text-align: center; }
  .card--back { left: 631px; background: var(--lime); text-align: center; }

  .tab { position: absolute; left: 102px; width: 143px; }
  .tab--top { top: 0; height: 31px; background: var(--plum); }
  .tab--bottom { bottom: 0; height: 28px; background: var(--magenta); }

  .brand-dot {
    position: absolute; left: 138px; top: 88px;
    width: 70px; height: 70px; border-radius: 50%;
    background: var(--lime);
  }
  .brand-name {
    position: absolute; left: 0; right: 0; top: 190px;
    font-size: 22px; font-weight: 300; letter-spacing: 2px;
    color: var(--grey);
  }
  .rule {
    position: absolute; left: 45px; width: 256px; top: 229px;
    height: 3px; background: var(--lime-line);
  }
  .tagline {
    position: absolute; left: 0; right: 0; top: 245px;
    font-size: 16px; font-weight: 300; color: var(--grey);
  }
  .person-name {
    position: absolute; left: 0; right: 0; top: 291px;
    font-size: 22px; font-weight: 600; color: var(--magenta);
  }
  .person-title {
    position: absolute; left: 0; right: 0; top: 319px;
    font-size: 15px; color: var(--plum);
  }
  .contacts {
    position: absolute; left: 0; right: 0; top: 366px;
    list-style: none; font-size: 15px; color: var(--plum);
  }
  .contacts li { height: 23.5px; line-height: 23px; }
  .contacts svg { width: 11px; height: 11px; vertical-align: -1px; margin-right: 7px; fill: var(--magenta); }
  .address {
    position: absolute; left: 0; right: 0; top: 454px;
    font-size: 15px; line-height: 21px; color: var(--plum);
  }

  .back-brand {
    position: absolute; left: 0; right: 0; top: 222px;
    font-size: 44px; font-weight: 600; color: var(--orange);
  }
  .back-name {
    position: absolute; left: 0; right: 0; top: 338px;
    font-size: 17px; letter-spacing: 1.5px; color: var(--ink);
  }
  .back-rule {
    position: absolute; left: 28px; width: 290px; top: 364px;
    height: 4px; background: var(--orange);
  }
  .back-title {
    position: absolute; left: 0; right: 0; top: 370px;
    font-size: 17px; letter-spacing: 1.5px; color: var(--ink);
  }
</style>
</head>
<body>
  <section class="card card--front">
    <div class="tab tab--top"></div>
    <div class="brand-dot"></div>
    <p class="brand-name">plumwave</p>
    <div class="rule"></div>
    <p class="tagline">Medier til unge</p>
    <h1 class="person-name">Asger Lindholm</h1>
    <p class="person-title">Salgsdirektor</p>
    <ul class="contacts">
      <li><svg viewBox="0 0 12 12" aria-hidden="true"><path d="M2.5 0.5 L4.5 0.5 L5.2 3.2 L3.8 4.4 C4.5 6 6 7.5 7.6 8.2 L8.8 6.8 L11.5 7.5 L11.5 9.5 C11.5 10.6 10.6 11.5 9.5 11.5 C4.5 11.2 0.8 7.5 0.5 2.5 C0.5 1.4 1.4 0.5 2.5 0.5 Z"/></svg>+45 20 31 42 53</li>
      <li><svg viewBox="0 0 12 12" aria-hidden="true"><path d="M0.5 2 H11.5 V10 H0.5 Z M1.5 3 L6 6.6 L10.5 3 V3 Z" fill-rule="evenodd"/></svg>al@plumwave.dk</li>
      <li><svg viewBox="0 0 12 12" aria-hidden="true"><circle cx="6" cy="6" r="5.5"/></svg>www.plumwave.dk</li>
    </ul>
    <p class="address">Kongevejens Allé 14 - 2100<br>Østerbro -Tlf. 31 62 47 90</p>
    <div class="tab tab--bottom"></div>
  </section>

  <section class="card card--back">
    <p class="back-brand">plumwave</p>
    <p class="back-name">Asger Lindholm</p>
    <div class="back-rule"></div>
    <p class="back-title">Salgsdirektør</p>
  </section>
</body>
</html>
```